We Need a Letterhead + Fax Cover Sheet for Heron Staffing

LETTERHEAD:
- Simple letterhead. Please provide an editable .doc file apart from usual Source Files. Logo Files attached for your use.
- Please place our logo on the upper right corner of the page. You may add some sort of graphic, or light colored background (depends on what looks good).
- Footer should include:
Heron Staffing, LLC
412 Kestrel Ave. Suite 118
Mobile, AL 36619

FAX COVER SHEET:
- Have the logo placed here, should be large, maybe an eight of the page.
- Put:
From:
To:
Phone Number:
Fax Number:

*Still needs some details, will update you because working on the website, etc.

Heron Coastal Workforce Services

```html
<!DOCTYPE html>
<html lang="en">
<head>
<meta charset="utf-8">
<title>Heron Staffing – Fax Cover Sheet</title>
<link href="https://fonts.googleapis.com/css2?family=Open+Sans:wght@400;600;700;800&display=swap" rel="stylesheet">
<style>
  :root {
    --backdrop: #dcdcdc;
    --paper: #ffffff;
    --brand-green: #8fa62a;
    --brand-blue: #1a6fb3;
    --watermark: #ececec;
    --footer-text: #555555;
  }
  * { box-sizing: border-box; margin: 0; padding: 0; }
  html, body {
    width: 1200px; height: 784px; overflow: hidden;
    background: var(--backdrop);
    font-family: "Open Sans", sans-serif;
  }
  .canvas {
    width: 1200px; height: 784px;
    display: flex; align-items: center; justify-content: center;
  }
  .fax-sheet {
    position: relative;
    width: 566px; height: 732px;
    background: var(--paper);
    border-top: 4px solid var(--brand-green);
    box-shadow: 0 2px 6px rgba(0,0,0,.12);
    overflow: hidden;
  }
  .brand {
    position: absolute; top: 24px; right: 28px;
    display: flex; align-items: center; gap: 8px;
  }
  .brand-dot {
    flex: none; width: 34px; height: 34px; border-radius: 50%;
    background: var(--brand-blue);
  }
  .brand-name {
    color: var(--brand-green); font-weight: 800;
    font-size: 13px; line-height: 1.15; text-transform: uppercase;
    width: 150px;
  }
  .fax-fields {
    position: absolute; top: 112px; left: 28px; right: 28px;
    display: grid; grid-template-columns: 1fr 1fr; column-gap: 22px; row-gap: 14px;
  }
  .field {
    display: flex; align-items: flex-end; gap: 4px;
    color: var(--brand-blue); font-weight: 700; font-size: 8px; white-space: nowrap;
  }
  .field-line { flex: 1; border-bottom: 1px solid var(--brand-blue); height: 1px; }
  .fax-fields .to-col { grid-column: 2; }
  .watermark {
    position: absolute; top: 270px; left: 0; right: 0;
    text-align: center;
    font-size: 170px; font-weight: 800; color: var(--watermark);
    letter-spacing: 0; line-height: 1;
  }
  .sheet-footer {
    position: absolute; left: 0; right: 0; bottom: 0;
  }
  .contact-line {
    display: flex; align-items: center; gap: 4px; flex-wrap: nowrap;
    padding: 0 12px 8px; font-size: 8.4px; color: var(--footer-text); white-space: nowrap;
  }
  .contact-icon { width: 8px; height: 8px; flex: none; }
  .footer-bands { display: flex; align-items: flex-end; height: 8px; }
  .band-green { width: 72%; height: 6px; background: var(--brand-green); }
  .band-blue { flex: 1; height: 8px; background: var(--brand-blue); margin-left: 8px; }
</style>
</head>
<body>
<main class="canvas">
  <article class="fax-sheet">
    <header class="brand">
      <span class="brand-dot"></span>
      <span class="brand-name">Heron Coastal Workforce Services</span>
    </header>

    <section class="fax-fields">
      <div class="field"><span>From:</span><span class="field-line"></span></div>
      <div class="field to-col"><span>To:</span><span class="field-line"></span></div>
      <div class="field"><span>Phone Number:</span><span class="field-line"></span></div>
      <div class="field to-col"><span>Fax Number:</span><span class="field-line"></span></div>
    </section>

    <div class="watermark" aria-hidden="true">FAX</div>

    <footer class="sheet-footer">
      <p class="contact-line">
        <svg class="contact-icon" viewBox="0 0 10 10"><circle cx="5" cy="5" r="5" fill="#1a6fb3"/><path d="M5 2.2a2 2 0 0 1 2 2c0 1.5-2 3.6-2 3.6S3 5.7 3 4.2a2 2 0 0 1 2-2z" fill="#fff"/></svg>
        <span>412 Kestrel Ave. Suite 118 Mobile, AL 36619</span>
        <svg class="contact-icon" viewBox="0 0 10 10"><circle cx="5" cy="5" r="5" fill="#1a6fb3"/><rect x="3.4" y="2.3" width="3.2" height="5.4" rx=".6" fill="#fff"/></svg>
        <span>(000) 000 0200</span>
        <svg class="contact-icon" viewBox="0 0 10 10"><circle cx="5" cy="5" r="5" fill="#1a6fb3"/><rect x="2.6" y="3" width="4.8" height="4" fill="#fff"/></svg>
        <span>(000) 000 0200</span>
        <svg class="contact-icon" viewBox="0 0 10 10"><circle cx="5" cy="5" r="5" fill="#1a6fb3"/><rect x="2.5" y="3.2" width="5" height="3.6" fill="#fff"/><path d="M2.5 3.2 5 5.2 7.5 3.2" stroke="#1a6fb3" stroke-width=".6" fill="none"/></svg>
        <span>info@heroncoastal.com</span>
        <svg class="contact-icon" viewBox="0 0 10 10"><circle cx="5" cy="5" r="5" fill="#1a6fb3"/><circle cx="5" cy="5" r="2.6" stroke="#fff" stroke-width=".7" fill="none"/><path d="M2.4 5h5.2M5 2.4v5.2" stroke="#fff" stroke-width=".6"/></svg>
        <span>heroncoastal.com</span>
      </p>
      <div class="footer-bands">
        <span class="band-green"></span>
        <span class="band-blue"></span>
      </div>
    </footer>
  </article>
</main>
</body>
</html>
```